BriskwayLane.com needs updated website design.

BriskwayLane.com offers individuals a quick, hassle-free way of selling their car, rv, or boat in the Cedar Bay Park, FL Area. We will come to the customer's place of choosing in order to give them an in-person offer for their car, rv, or boat. Looking for a website design that will allow users to input their vehicle details as well as their contact info in order to schedule a time and place for our staff to come make them an offer. Currently have an active site that can be referenced.

Target Market(s)

Older people who no longer need their cars.

Industry/Entity Type

Automotive

Coding

Coded - Design and coding required

Number of Pages Required

3 page

Font styles to use
Sans Serif

Colors
a1cd3a
33b8a4

Requirements
Must have
• Trustworthy theme, Emphasis on capturing contact info (contact form visible at all times). Standard privacy policy. Wordpress theme

```html
<!DOCTYPE html>
<html lang="en">
<head>
<meta charset="utf-8">
<title>BriskwayLane.com – We Buy Cars, RVs &amp; Boats</title>
<link href="https://fonts.googleapis.com/css2?family=Poppins:wght@400;500;600;700&display=swap" rel="stylesheet">
<style>
:root{
  --lime:#a1cd3a;
  --teal:#33b8a4;
  --teal-dark:#2aa391;
  --ink:#333333;
  --charcoal:#3a3a3a;
  --white:#ffffff;
  --text:#2b2b2b;
  --olive:#3b4a2a;
}
*{margin:0;padding:0;box-sizing:border-box}
html,body{width:1200px;height:4487px;overflow:hidden}
body{font-family:'Poppins',sans-serif;background:var(--white);color:var(--text);position:relative}
.abs{position:absolute}
.photo{position:absolute}
.btn{position:absolute;display:flex;align-items:center;justify-content:center;gap:8px;font-weight:600;color:var(--white);border-radius:6px}
.btn-teal{background:var(--teal);box-shadow:0 3px 6px rgba(0,0,0,.3)}
.btn-lime{background:var(--lime);box-shadow:0 2px 4px rgba(0,0,0,.2)}
.btn-dark{background:var(--olive);color:var(--lime);border-radius:18px;box-shadow:0 3px 6px rgba(0,0,0,.45)}
.arrow{width:20px;height:14px}
.seam{position:absolute;width:52px;height:52px;border-radius:50%;background:var(--olive);border:4px solid var(--lime);z-index:5}
.seam::after{content:"";position:absolute;inset:12px;border-radius:50%;background:var(--teal)}

/* hero */
.hero{position:absolute;left:0;top:0;width:1200px;height:833px}
.hero-band{position:absolute;left:0;top:0;width:1200px;height:833px;background:var(--lime);border-radius:0 0 60px 60px}
.hero-photo{left:0;top:0;width:1200px;height:800px;border-radius:0 0 60px 60px;background:radial-gradient(ellipse at 55% 40%,#4d4d4d 0%,#2f2f2f 55%,#1f1f1f 100%)}
.nav{position:absolute;left:155px;top:23px;width:927px;height:90px;background:var(--white);display:flex;align-items:center}
.nav-green{position:absolute;right:0;top:0;width:228px;height:90px;background:var(--lime)}
.brand{position:absolute;left:34px;top:20px;font-size:20px;font-weight:700;color:var(--ink);white-space:nowrap}
.brand small{display:block;font-size:11px;font-weight:600;color:var(--lime)}
.brand-dot{position:absolute;left:252px;top:22px;width:46px;height:46px;border-radius:50%;background:var(--teal)}
.nav a{position:absolute;top:33px;font-size:18px;font-weight:600;color:var(--ink);text-decoration:none}
.nav .home{left:385px;background:var(--lime);padding:0 4px}
.nav .signup{background:var(--olive);color:var(--lime);border-radius:14px;padding:1px 8px;font-size:17px;top:31px}
.hero-rule{left:118px;top:262px;width:4px;height:252px;background:var(--lime)}
.hero-title{left:155px;top:258px;font-size:40px;font-weight:700;color:var(--white);letter-spacing:-.5px}
.hero-title span{color:var(--lime)}
.socials{left:0;top:322px;display:flex;flex-direction:column;gap:6px}
.socials div{width:48px;height:36px;background:var(--lime);border-radius:0 6px 6px 0;display:flex;align-items:center;justify-content:center}
.dots{left:557px;top:768px;display:flex;gap:9px}
.dots i{width:13px;height:13px;border-radius:50%;background:var(--lime);display:block}
.hero-form{left:859px;top:258px;width:270px;height:404px;background:var(--teal);box-shadow:10px 6px 0 var(--lime)}
.hero-form h3{position:absolute;left:46px;top:40px;font-size:25px;font-weight:500;color:var(--ink)}
.field{position:absolute;left:14px;width:242px;display:flex;align-items:flex-end;gap:10px;font-size:19px;font-weight:600;color:var(--white)}
.field i{flex:1;height:2px;background:var(--ink);margin-bottom:6px}

/* about */
.about-dark{left:854px;top:833px;width:346px;height:648px;background:var(--charcoal)}
.about-title{left:96px;top:1005px;font-size:36px;font-weight:700;color:var(--ink)}
.about-title span{color:var(--lime)}
.about-list{left:96px;top:1130px;list-style:none;font-size:25px;color:var(--ink);line-height:40px}
.about-list li{display:flex;align-items:center;gap:22px}
.about-photo{left:719px;top:995px;width:419px;height:285px;background:linear-gradient(120deg,#f2f5e6,#e4ead0 60%,#cbd3ae);box-shadow:0 8px 0 var(--lime),0 4px 14px rgba(0,0,0,.25)}
.about-brand{left:96px;top:1325px;font-size:52px;font-weight:700;color:#6a6a6a}
.about-brand small{display:block;font-size:32px;font-weight:600;color:var(--lime);margin-top:-6px}

/* three tiles */
.tiles{left:0;top:1486px;width:1200px;height:477px;background:var(--teal)}
.tile{position:absolute;top:0;height:477px;width:1200px}
.tile h4{position:absolute;font-size:31px;font-weight:700;color:var(--white);line-height:70px;text-shadow:0 2px 3px rgba(0,0,0,.4)}
.tile .btn{font-size:19px;height:46px;width:172px}

/* feature rows */
.row{position:absolute;left:0;width:1200px;background:var(--teal)}
.row h2{position:absolute;font-size:40px;font-weight:700;color:var(--white);padding:2px 14px;box-shadow:6px 6px 0 rgba(255,255,255,.25)}
.row p{position:absolute;font-size:25px;font-weight:500;color:var(--white);line-height:40px}
.row .rule{position:absolute;width:4px;background:var(--lime)}
.row .btn{font-size:19px;height:38px;padding:0 14px}

/* contact */
.contact{left:0;top:3268px;width:1200px;height:690px;background:var(--white)}
.contact-title{left:131px;top:138px;width:296px;height:75px;display:flex;align-items:center;justify-content:center;font-size:34px;font-weight:700;color:var(--teal);box-shadow:0 2px 10px rgba(0,0,0,.18)}
.contact-rule{left:92px;top:250px;width:4px;height:420px;background:var(--ink)}
.c-item{left:122px;display:flex;align-items:center;gap:30px;font-size:25px;color:var(--teal)}
.c-item svg{width:44px;height:44px}
.hours{left:130px;top:583px;font-size:31px;color:var(--lime);display:flex;align-items:center;gap:40px}
.hours span{font-size:25px;color:var(--ink)}
.hours i{width:2px;height:30px;background:var(--ink)}
.keys-photo{left:714px;top:130px;width:105px;height:190px;border-radius:40px;background:linear-gradient(160deg,#e9c4a3,#2d2d2d 70%)}
.form-back{left:846px;top:135px;width:306px;height:533px;background:#bfe6df}
.form-box{left:854px;top:143px;width:292px;height:517px;background:var(--lime)}
.form-box .field{color:var(--ink);font-weight:500;font-size:21px;left:16px;width:260px}

/* footer */
.footer{left:0;top:3958px;width:1200px;height:529px;background:var(--charcoal)}
.foot-logo{left:57px;top:44px;width:330px;height:92px;background:var(--white)}
.foot-logo .brand{left:38px;top:24px;font-size:18px}
.foot-logo .brand small{font-size:10px}
.foot-logo .brand-dot{left:240px;top:22px;width:46px;height:46px}
.foot-tag{left:47px;top:168px;font-size:20px;font-weight:500;color:var(--white)}
.foot-h{font-size:30px;font-weight:700;color:var(--teal)}
.foot-item{left:47px;display:flex;align-items:center;gap:20px;font-size:16px;color:var(--white)}
.foot-item svg{width:30px;height:30px}
.blog{left:550px;top:290px;list-style:none;font-size:20px;color:var(--white);line-height:44px}
.copy{left:0;top:490px;width:1200px;text-align:center;font-size:20px;font-weight:700;color:var(--white)}
.map{left:820px;top:0;width:380px;height:529px;background:linear-gradient(150deg,#eef0ea,#e2e6dc 50%,#d7dccf);clip-path:polygon(10px 0,100% 0,100% 100%,10px 100%,60px 50%)}
</style>
</head>
<body>

<!-- HERO -->
<section class="hero">
  <div class="hero-band"></div>
  <div class="photo hero-photo" role="img" aria-label="Hand holding out car keys in front of a blurred dark car"></div>
  <svg class="abs" style="left:0;top:0" width="1200" height="800" aria-hidden="true">
    <g stroke="#a1cd3a" stroke-width="2" fill="none">
      <polyline points="860,400 800,450 860,500"/>
      <polyline points="870,385 810,450 870,515"/>
      <line x1="1060" y1="340" x2="1200" y2="230"/>
      <line x1="1050" y1="300" x2="1200" y2="180"/>
    </g>
  </svg>
  <nav class="nav">
    <div class="nav-green"></div>
    <div class="brand">BriskwayLane.com<small>I'll Buy You Car Boat RV Today</small></div>
    <div class="brand-dot"></div>
    <a class="home" href="#">HOME</a>
    <a href="#" style="left:499px">SERVICES</a>
    <a href="#" style="left:650px">CONTACT</a>
    <a class="signup" href="#" style="left:795px">SIGN UP</a>
  </nav>
  <div class="abs hero-rule"></div>
  <h1 class="abs hero-title">WE BUY <span>CARS RV'S</span> &amp; <span>BOATS</span></h1>
  <div class="btn btn-teal" style="left:157px;top:448px;width:243px;height:54px;font-size:25px">GET STARTED
    <svg class="arrow" viewBox="0 0 20 14"><path d="M2 2h6l5 5-5 5H2l5-5z" fill="#fff"/></svg></div>
  <div class="abs socials" aria-label="Social links">
    <div><svg width="20" height="20" viewBox="0 0 20 20"><rect x="3" y="3" width="14" height="14" rx="2" fill="none" stroke="#333" stroke-width="2"/></svg></div>
    <div><svg width="20" height="20" viewBox="0 0 20 20"><circle cx="10" cy="10" r="7" fill="none" stroke="#333" stroke-width="2"/></svg></div>
    <div><svg width="20" height="20" viewBox="0 0 24 24"><path d="M6 3l3 4-2 2c1 3 4 6 7 7l2-2 4 3-2 4C10 21 3 14 3 5z" fill="none" stroke="#333" stroke-width="2"/></svg></div>
  </div>
  <div class="abs dots"><i></i><i></i><i></i><i></i></div>
  <form class="abs hero-form">
    <h3>WE BUY CARS</h3>
    <div class="field" style="top:114px">Name<i></i></div>
    <div class="field" style="top:178px">Email<i></i></div>
    <div class="field" style="top:242px">Phone<i></i></div>
    <div class="btn btn-dark" style="left:62px;top:326px;width:150px;height:50px;font-size:18px">SELL VEHICLES</div>
  </form>
</section>

<!-- ABOUT -->
<div class="abs about-dark"></div>
<svg class="abs" style="left:854px;top:833px" width="346" height="648" aria-hidden="true">
  <g stroke="#a1cd3a" stroke-width="3" fill="none">
    <line x1="130" y1="160" x2="346" y2="20"/><line x1="150" y1="160" x2="346" y2="40"/>
    <line x1="200" y1="400" x2="346" y2="520"/><line x1="220" y1="380" x2="346" y2="480"/>
  </g>
</svg>
<h2 class="abs about-title">“Don’t <span>Sell</span> Till You Give Me A <span>Yell</span>”</h2>
<ul class="abs about-list">
  <li><svg width="18" height="14" viewBox="0 0 18 14"><path d="M1 7l5 5L17 1" stroke="#333" stroke-width="3" fill="none"/></svg>Fast – I’ll Be at Your Door Today.</li>
  <li><svg width="18" height="14" viewBox="0 0 18 14"><path d="M1 7l5 5L17 1" stroke="#333" stroke-width="3" fill="none"/></svg>Fair – Get Fair Price for Your Vehicle.</li>
  <li><svg width="18" height="14" viewBox="0 0 18 14"><path d="M1 7l5 5L17 1" stroke="#333" stroke-width="3" fill="none"/></svg>Friendly – Trusted for Over 25 Years.</li>
  <li><svg width="18" height="14" viewBox="0 0 18 14"><path d="M1 7l5 5L17 1" stroke="#333" stroke-width="3" fill="none"/></svg>Hassle Free – I Handle All the Paperwork.</li>
</ul>
<div class="photo about-photo" role="img" aria-label="One hand passing car keys while another hands over cash"></div>
<div class="abs about-brand">BriskwayLane.com<small>I'll Buy You Car Boat RV Today</small></div>

<!-- THREE TILES -->
<section class="abs tiles">
  <div class="tile" style="clip-path:polygon(0 0,370px 0,440px 50%,370px 100%,0 100%)">
    <div class="photo" style="inset:0;background:linear-gradient(135deg,#9fb9c6,#e3d8a8 45%,#6f8a3a)" role="img" aria-label="Motorhome RV parked outdoors"></div>
    <h4 style="left:17px;top:80px">We Buy RV’s<br>On Any Conditioned</h4>
    <div class="btn btn-dark" style="left:17px;top:277px">SELL VEHICLES</div>
  </div>
  <div class="tile" style="clip-path:polygon(370px 0,800px 0,870px 50%,800px 100%,370px 100%,440px 50%)">
    <div class="photo" style="inset:0;background:linear-gradient(135deg,#c58a2a,#5a4a2a 50%,#23344e)" role="img" aria-label="Blue car parked at sunset"></div>
    <h4 style="left:410px;top:80px">We Buy Car’s<br>On Any Conditioned</h4>
    <div class="btn btn-dark" style="left:410px;top:277px">SELL VEHICLES</div>
  </div>
  <div class="tile" style="clip-path:polygon(800px 0,1200px 0,1200px 100%,800px 100%,870px 50%)">
    <div class="photo" style="inset:0;background:linear-gradient(150deg,#3e6fa8,#6a5aa8 50%,#c8d3e0)" role="img" aria-label="Speedboat cutting through blue water"></div>
    <h4 style="left:841px;top:80px">We Buy Boat’s<br>On Any Conditioned</h4>
    <div class="btn btn-dark" style="left:841px;top:277px">SELL VEHICLES</div>
  </div>
</section>
<div class="seam" style="left:827px;top:1460px"></div>
<div class="seam" style="left:823px;top:1937px"></div>

<!-- OLD CLUNKER -->
<section class="row" style="top:1963px;height:450px">
  <div class="photo" style="left:0;top:0;width:819px;height:450px;clip-path:polygon(0 0,819px 0,575px 100%,0 100%);background:linear-gradient(120deg,#9bb3bd,#c9b98a 45%,#6d7a7c)" role="img" aria-label="Two rusty vintage cars parked by a weathered wall"></div>
  <h2 style="left:843px;top:82px">Old Clunker</h2>
  <div class="rule" style="left:827px;top:178px;height:160px"></div>
  <p style="left:857px;top:183px">“Got an old Clunker?<br>I’ll But It! – Turn it into<br>Cash today!”</p>
  <div class="btn btn-lime" style="left:857px;top:327px">Sell Clunkers
    <svg class="arrow" viewBox="0 0 20 14"><path d="M2 2h6l5 5-5 5H2l5-5z" fill="#fff"/></svg></div>
</section>
<div class="seam" style="left:538px;top:2387px"></div>

<!-- DON'T NEED -->
<section class="row" style="top:2413px;height:430px">
  <div class="photo" style="left:0;top:0;width:1200px;height:430px;clip-path:polygon(575px 0,1200px 0,1200px 100%,819px 100%);background:linear-gradient(130deg,#3a2a2e,#7a3a3a 45%,#2a2f3a)" role="img" aria-label="Hands counting a stack of cash"></div>
  <h2 style="left:125px;top:40px">Dont’ Need</h2>
  <div class="rule" style="left:92px;top:135px;height:200px"></div>
  <p style="left:133px;top:135px">“Got a nice car you just don’t need?<br>I’ll Buy It! – Stop wasting money<br>on insurance, registration &amp;<br>maintenance costs!”</p>
  <div class="btn btn-lime" style="left:133px;top:325px">Sell Nice Car
    <svg class="arrow" viewBox="0 0 20 14"><path d="M2 2h6l5 5-5 5H2l5-5z" fill="#fff"/></svg></div>
</section>
<div class="seam" style="left:800px;top:2817px"></div>

<!-- I'LL BUY IT -->
<section class="row" style="top:2843px;height:425px">
  <div class="photo" style="left:0;top:0;width:819px;height:425px;clip-path:polygon(0 0,819px 0,575px 100%,0 100%);background:linear-gradient(130deg,#3f5a2a,#7a9a4a 50%,#2a3a2a)" role="img" aria-label="Frustrated driver beside a car with its hood open"></div>
  <h2 style="left:822px;top:48px">I’ll Buy It</h2>
  <div class="rule" style="left:830px;top:135px;height:180px"></div>
  <p style="left:846px;top:135px;line-height:35px">“Got a car that needs<br>repairs? I’ll Buy It!<br>No matter what<br>the issue is I’ll come take<br>it away today!”</p>
  <div class="btn btn-lime" style="left:846px;top:335px">Sell Nice Car
    <svg class="arrow" viewBox="0 0 20 14"><path d="M2 2h6l5 5-5 5H2l5-5z" fill="#fff"/></svg></div>
</section>
<div class="seam" style="left:539px;top:3242px"></div>

<!-- CONTACT -->
<section class="abs contact">
  <svg class="abs" style="left:0;top:0" width="1200" height="690" aria-hidden="true">
    <line x1="566" y1="0" x2="810" y2="690" stroke="#a1cd3a" stroke-width="3"/>
  </svg>
  <h2 class="abs contact-title">CONTACT INFO</h2>
  <div class="abs contact-rule"></div>
  <div class="abs c-item" style="top:268px">
    <svg viewBox="0 0 24 24"><path d="M12 2a7 7 0 0 0-7 7c0 5 7 12 7 12s7-7 7-12a7 7 0 0 0-7-7z" fill="none" stroke="#a1cd3a" stroke-width="1.6"/><circle cx="12" cy="9" r="2.5" fill="none" stroke="#a1cd3a" stroke-width="1.6"/></svg>
    CEDAR BAY PARK, FL AREA</div>
  <div class="abs c-item" style="top:373px">
    <svg viewBox="0 0 24 24"><rect x="2" y="6" width="20" height="14" fill="none" stroke="#a1cd3a" stroke-width="1.6"/><path d="M2 6l10 8 10-8" fill="none" stroke="#a1cd3a" stroke-width="1.6"/></svg>
    https://briskwaylane.com</div>
  <div class="abs c-item" style="top:478px">
    <svg viewBox="0 0 24 24"><path d="M6 3l3 4-2 2c1 3 4 6 7 7l2-2 4 3-2 4C10 21 3 14 3 5z" fill="none" stroke="#a1cd3a" stroke-width="1.6"/></svg>
    0300-555-0147 | 021-555-0199</div>
  <div class="abs hours">Opening Hours<i></i><span>9:00 AM to 9:00 PM</span></div>
  <div class="photo keys-photo" role="img" aria-label="Hand holding a car key"></div>
  <div class="abs form-back"></div>
  <form class="abs form-box" aria-label="Vehicle offer request">
    <div class="field" style="top:48px">Name<i></i></div>
    <div class="field" style="top:122px">Email<i></i></div>
    <div class="field" style="top:198px">Phone<i></i></div>
    <div class="field" style="top:273px">Address<i></i></div>
    <div class="field" style="top:348px">Details<i></i></div>
    <div class="field" style="top:412px"><i></i></div>
    <div class="btn btn-dark" style="left:80px;top:448px;width:124px;height:40px;font-size:15px">SELL VEHICLES</div>
  </form>
</section>
<div class="seam" style="left:787px;top:3932px"></div>

<!-- FOOTER -->
<footer class="abs footer">
  <div class="photo map" role="img" aria-label="Street map of the local service area"></div>
  <div class="abs foot-logo">
    <div class="brand">BriskwayLane.com<small>I'll Buy You Car Boat RV Today</small></div>
    <div class="brand-dot"></div>
  </div>
  <div class="abs foot-tag">Get You Free In Person Cash Offer Today</div>
  <div class="btn btn-teal" style="left:540px;top:118px;width:188px;height:40px;font-size:20px">GET STARTED
    <svg class="arrow" viewBox="0 0 20 14"><path d="M2 2h6l5 5-5 5H2l5-5z" fill="#fff"/></svg></div>
  <h3 class="abs foot-h" style="left:49px;top:215px">Contact Info</h3>
  <h3 class="abs foot-h" style="left:545px;top:215px">Our Blog</h3>
  <div class="abs foot-item" style="top:290px">
    <svg viewBox="0 0 24 24"><path d="M12 2a7 7 0 0 0-7 7c0 5 7 12 7 12s7-7 7-12a7 7 0 0 0-7-7z" fill="none" stroke="#a1cd3a" stroke-width="1.6"/><circle cx="12" cy="9" r="2.5" fill="none" stroke="#a1cd3a" stroke-width="1.6"/></svg>
    CEDAR BAY PARK, FL AREA</div>
  <div class="abs foot-item" style="top:358px">
    <svg viewBox="0 0 24 24"><rect x="2" y="6" width="20" height="14" fill="none" stroke="#a1cd3a" stroke-width="1.6"/><path d="M2 6l10 8 10-8" fill="none" stroke="#a1cd3a" stroke-width="1.6"/></svg>
    https://briskwaylane.com</div>
  <div class="abs foot-item" style="top:426px">
    <svg viewBox="0 0 24 24"><path d="M6 3l3 4-2 2c1 3 4 6 7 7l2-2 4 3-2 4C10 21 3 14 3 5z" fill="none" stroke="#a1cd3a" stroke-width="1.6"/></svg>
    0300-555-0147 | 021-555-0199</div>
  <ul class="abs blog">
    <li>Most people who Who Order</li>
    <li>To Get More Efficiency</li>
    <li>How To Improve Selling</li>
  </ul>
  <div class="abs copy">Copyright © All right reserved</div>
</footer>
<div class="seam" style="left:786px;top:4460px"></div>

</body>
</html>
```